Bramble Artisan Wood Fired Pizza business card design

I have a logo and need an eye catching design that will get me noticed.
My business is wood fired pizza. I want a bold design that will make our customers remember us and the food that we serve. Work with the colors of our logo and texts. Maybe add designs that lend to what or how pizza is made using our wood fired oven?

Target Market(s)

Foodies!

Contact Information for Business Card

Bramble Artisan Wood Fired Pizza
Our slogan is Fast. Fresh. Handcrafted
Catering for all events

Requirements
Must have
• Noel Pruett
Telephone 570 555 0187
website www.trybramble.com
Facebook @trybramblepizza maybe use the facebook logo next to it
Instagram trybramblepizza maybe use the instagram logo next to it
Catering for all events
Nice to have
• Maybe pizza peels, pizza cutters? Wood? Fired wood? Using our flame in the background?
Please work with different colored text so each sentence stands out? A themed color for facebook?
Maybe work with the colors within our logo?
Please try to use the our bramble font, but not a must have.

```html
<!DOCTYPE html>
<html lang="en">
<head>
<meta charset="utf-8">
<title>Bramble Artisan Wood Fired Pizza – Business Card</title>
<link rel="stylesheet" href="https://fonts.googleapis.com/css2?family=Roboto:wght@500;700&family=Work+Sans:wght@400&display=swap">
<style>
  :root {
    --page-bg: #e9e4de;
    --card-bg: #f6f5f3;
    --card-edge: #dcd8d3;
    --brand-red: #c8141b;
    --brand-black: #252422;
    --brand-orange: #d9780f;
    --text-dark: #3a3836;
    --text-mid: #55524f;
  }
  html, body {
    margin: 0;
    padding: 0;
    width: 1200px;
    height: 887px;
    overflow: hidden;
    background: var(--page-bg);
  }
  .business-card {
    position: absolute;
    left: 120px;
    top: 183px;
    width: 960px;
    height: 520px;
    background: var(--card-bg);
    border: 1px solid var(--card-edge);
    border-radius: 22px;
    overflow: hidden;
    box-shadow: 0 10px 30px rgba(60, 45, 30, 0.15);
  }
  .brand-block {
    position: absolute;
    left: 0;
    top: 140px;
    width: 440px;
    height: 250px;
    display: flex;
    flex-direction: column;
    align-items: center;
    justify-content: center;
    gap: 22px;
  }
  .brand-dot {
    width: 90px;
    height: 90px;
    border-radius: 50%;
    background: var(--brand-red);
  }
  .brand-name {
    font-family: "Roboto", sans-serif;
    font-weight: 700;
    font-size: 24px;
    line-height: 1.25;
    color: var(--brand-black);
    text-align: center;
    letter-spacing: 1px;
    text-transform: uppercase;
    margin: 0;
  }
  .divider {
    position: absolute;
    left: 440px;
    top: 142px;
    width: 2px;
    height: 248px;
    background: var(--brand-red);
  }
  .contact-block {
    position: absolute;
    left: 532px;
    top: 132px;
  }
  .person-name {
    font-family: "Roboto", sans-serif;
    font-weight: 500;
    font-size: 37px;
    line-height: 40px;
    color: var(--brand-red);
    letter-spacing: 0.5px;
    text-transform: uppercase;
    margin: 0;
  }
  .person-role {
    font-family: "Work Sans", sans-serif;
    font-size: 23px;
    line-height: 28px;
    color: var(--text-mid);
    letter-spacing: 0.5px;
    margin: 2px 0 14px;
  }
  .contact-list {
    list-style: none;
    margin: 0;
    padding: 0;
    font-family: "Work Sans", sans-serif;
    font-size: 23.5px;
    color: var(--text-dark);
    letter-spacing: 0.6px;
  }
  .contact-list li {
    display: flex;
    align-items: center;
    gap: 8px;
    height: 30px;
  }
  .contact-list .group-gap { margin-top: 14px; }
  .icon { width: 16px; height: 16px; flex: none; }
  .social-square {
    width: 13px;
    height: 13px;
    margin: 0 1px 0 2px;
    border-radius: 2px;
    background: var(--brand-red);
    flex: none;
  }
  .color-band {
    position: absolute;
    left: 0;
    bottom: 0;
    width: 100%;
    height: 27px;
    display: flex;
  }
  .color-band span { flex: 1; }
  .band-red { background: var(--brand-red); }
  .band-black { background: var(--brand-black); }
  .band-orange { background: var(--brand-orange); }
</style>
</head>
<body>
  <article class="business-card">
    <div class="brand-block">
      <div class="brand-dot"></div>
      <p class="brand-name">Bramble Artisan<br>Wood Fired Pizza</p>
    </div>

    <div class="divider"></div>

    <div class="contact-block">
      <h1 class="person-name">Noel Pruett</h1>
      <p class="person-role">Founder</p>
      <ul class="contact-list">
        <li><span class="social-square"></span>trybramblepizza</li>
        <li><span class="social-square"></span>trybramblepizza</li>
        <li class="group-gap">
          <svg class="icon" viewBox="0 0 16 16" aria-hidden="true">
            <path d="M4 1.5l2.2 2.6-1.3 1.6c.9 2 2.4 3.5 4.4 4.4l1.6-1.3 2.6 2.2-1.4 2.2C7.5 13 3 8.5 1.8 2.9z" fill="var(--brand-red)"/>
          </svg>570 555 0187</li>
        <li>
          <svg class="icon" viewBox="0 0 16 16" aria-hidden="true">
            <rect x="1.5" y="3.5" width="13" height="9" fill="none" stroke="var(--brand-red)" stroke-width="1.6"/>
            <path d="M1.8 4l6.2 4.6L14.2 4" fill="none" stroke="var(--brand-red)" stroke-width="1.6"/>
          </svg>info@trybramble.com</li>
        <li>
          <svg class="icon" viewBox="0 0 16 16" aria-hidden="true">
            <g fill="none" stroke="var(--brand-red)" stroke-width="1.4">
              <circle cx="8" cy="8" r="6.3"/>
              <ellipse cx="8" cy="8" rx="2.8" ry="6.3"/>
              <path d="M1.7 8h12.6M2.8 4.8h10.4M2.8 11.2h10.4"/>
            </g>
          </svg>www.trybramble.com</li>
      </ul>
    </div>

    <div class="color-band">
      <span class="band-red"></span>
      <span class="band-black"></span>
      <span class="band-orange"></span>
    </div>
  </article>
</body>
</html>
```